Presentation Folder for dental clinic

We need a presentation folder design. The presentation folder is what we give to our patients with treatment plans, quotes, images, information sheets etc.
I have uploaded current stationary designs for assistance as well as a photo of our external sign design.
We are an upmarket dental clinic.
Professionalism and customer service is key to us.
We provide information in presentation folders to give to patients.
It needs to memorable and a statement to who we are.

Target Market(s)

Main patient base is Male and Female 40 years old to 70 years old

Industry/Entity Type

Dental Clinic

Font styles to use
Serif
Sans Serif

Requirements
Must have
• Design:
• -Professional
• -Timeless
• -Modern
• - Memorable
• - Statement (if a patient puts down the folder, it will be easily identifiable with as Morvel Dentals folder)
• Logo
• Address, phone, email, website
• Dr Leon Brisco name and degree details
• Colour scheme to match current logos and branding
• "Your Smile Our Passion" quote
Nice to have
• Services listed:
• - Sleep Dentistry
• - Happy Gas
• - Dental Implants
• - Cosmetic Dentistry
• - Oral Surgery
• - Clearotune
• - Teeth Whitening
• - General Dentistry
• - Childrens Dentistry
• See website www.morveldental.com.au
Should not have
• Dental cliche photos

```html
<!DOCTYPE html>
<html lang="en">
<head>
<meta charset="utf-8">
<title>Morvel Dental Presentation Folder</title>
<link href="https://fonts.googleapis.com/css2?family=Exo+2:wght@500&family=Roboto:wght@400;500;700&family=Yesteryear&display=swap" rel="stylesheet">
<style>
  :root {
    --backdrop: #b4b4b7;
    --paper: #f4f4f5;
    --paper-shade: #e6e6e8;
    --purple: #7b3f94;
    --purple-light: #9c63b0;
    --purple-dark: #64307a;
    --grey-text: #9a9a9e;
    --white: #ffffff;
    --photo-top: #e9e9ec;
    --photo-mid: #4b5366;
    --photo-low: #c9ccd3;
    --pattern-a: #f7f4f8;
    --pattern-b: #ebe3ef;
  }
  * { box-sizing: border-box; margin: 0; padding: 0; }
  html, body { width: 842px; height: 1200px; overflow: hidden; background: var(--backdrop); }
  body { font-family: "Roboto", Arial, sans-serif; }
  .canvas { position: relative; width: 842px; height: 1200px; }

  .spread { position: absolute; left: 51px; width: 740px; height: 530px; display: flex; box-shadow: 0 10px 24px rgba(0,0,0,.22); }
  .spread--outer { top: 40px; }
  .spread--inner { top: 630px; }
  .panel { position: relative; width: 370px; height: 100%; overflow: hidden; }

  /* back cover */
  .back-cover { background: linear-gradient(115deg, var(--purple-dark), var(--purple-light) 45%, var(--purple) 100%); color: var(--white); }
  .back-details { position: absolute; left: 0; right: 0; bottom: 52px; text-align: center; line-height: 1.35; }
  .wordmark { font-family: "Exo 2", "Roboto", sans-serif; font-weight: 500; letter-spacing: -0.5px; }
  .back-details .wordmark { font-size: 17px; color: var(--white); margin-bottom: 4px; }
  .doctor-name { font-size: 10px; font-weight: 700; }
  .credentials { font-size: 7.5px; font-weight: 500; }
  .contact { font-size: 7px; margin-top: 8px; letter-spacing: .3px; }

  /* front cover */
  .front-cover { background: linear-gradient(135deg, var(--white), var(--paper) 60%, var(--paper-shade)); }
  .front-cover .wordmark { position: absolute; top: 48px; left: 48px; font-size: 38px; color: var(--purple); }
  .portrait { position: absolute; right: 14px; bottom: 40px; width: 185px; height: 215px;
    background: linear-gradient(180deg, var(--photo-top) 0%, var(--photo-mid) 35%, var(--photo-mid) 70%, var(--photo-low) 100%); }
  .tagline-band { position: absolute; right: 0; bottom: 0; width: 240px; height: 40px; background: var(--purple);
    clip-path: polygon(14% 0, 100% 0, 100% 100%, 0 100%); display: flex; align-items: center; justify-content: flex-end; padding-right: 14px; }
  .tagline { font-family: "Yesteryear", "Georgia", serif; font-size: 19px; color: var(--white); }

  /* inner spread */
  .inner-panel { background: var(--paper); }
  .inner-pattern { position: absolute; inset: 0; background: repeating-linear-gradient(90deg, var(--pattern-a) 0 22px, var(--pattern-b) 22px 24px); }
  .pocket { position: absolute; left: 0; right: 0; bottom: 0; height: 190px;
    background: linear-gradient(120deg, var(--purple-dark), var(--purple-light) 55%, var(--purple)); box-shadow: 0 -3px 8px rgba(0,0,0,.15); }
  .pocket--left { clip-path: polygon(0 0, 100% 14%, 100% 100%, 0 100%); }
  .pocket--right { clip-path: polygon(0 14%, 100% 0, 100% 100%, 0 100%); }
  .card-slits { position: absolute; left: 120px; top: 60px; }

  .services { position: absolute; left: 18px; right: 18px; top: 52px; color: var(--white); }
  .services-title { text-align: center; font-size: 12px; font-weight: 700; letter-spacing: 1px; margin-bottom: 12px; }
  .services-columns { display: flex; }
  .services-list { flex: 1; list-style: none; font-size: 9.5px; line-height: 1.55; padding: 0 10px; border-left: 1px solid rgba(255,255,255,.6); }
  .services-list:first-child { border-left: none; }
  .services-list li::before { content: "• "; }
  .social { display: flex; justify-content: center; gap: 5px; margin-top: 14px; }
  .social span { width: 10px; height: 10px; border-radius: 50%; background: var(--white); }
  .services-web { text-align: center; font-size: 8.5px; margin-top: 8px; letter-spacing: .3px; }
</style>
</head>
<body>
<main class="canvas">

  <section class="spread spread--outer" aria-label="Folder outer spread">
    <div class="panel back-cover">
      <div class="back-details">
        <p class="wordmark">Morvel Dental</p>
        <p class="doctor-name">Dr Leon Brisco &amp; Associates</p>
        <p class="credentials">B.D.S Westbridge College London</p>
        <p class="credentials">Graduate Diploma in Clinical Dentistry</p>
        <p class="credentials">(IV Sedation &amp; Pain Control) Coastline University</p>
        <p class="contact">214 HARBOUR RD, ELWOOD VIC 3184</p>
        <p class="contact" style="margin-top:0">03 9000 4417 | INFO@MORVELDENTAL.COM.AU</p>
        <p class="contact" style="margin-top:0">WWW.MORVELDENTAL.COM.AU</p>
      </div>
    </div>
    <div class="panel front-cover">
      <p class="wordmark">Morvel Dental</p>
      <div class="portrait" role="img" aria-label="Photo of the lead dentist leaning on the clinic reception desk"></div>
      <div class="tagline-band"><p class="tagline">Your Smile Our Passion</p></div>
    </div>
  </section>

  <section class="spread spread--inner" aria-label="Folder inner spread">
    <div class="panel inner-panel">
      <div class="inner-pattern" role="img" aria-label="Faint repeated clinic name pattern in pale lavender"></div>
      <div class="pocket pocket--left">
        <svg class="card-slits" width="80" height="90" viewBox="0 0 80 90" aria-hidden="true">
          <g stroke="#ffffff" stroke-width="1.2">
            <line x1="0" y1="6" x2="14" y2="4"/>
            <line x1="70" y1="40" x2="71" y2="52"/>
            <line x1="40" y1="86" x2="54" y2="84"/>
          </g>
        </svg>
      </div>
    </div>
    <div class="panel inner-panel">
      <div class="inner-pattern" role="img" aria-label="Faint repeated clinic name pattern in pale lavender"></div>
      <div class="pocket pocket--right">
        <div class="services">
          <p class="services-title">SERVICES</p>
          <div class="services-columns">
            <ul class="services-list">
              <li>Sleep Dentistry</li><li>Happy Gas</li><li>Dental Implants</li>
            </ul>
            <ul class="services-list">
              <li>Oral Surgery</li><li>Clearotune</li><li>Cosmetic Dentistry</li>
            </ul>
            <ul class="services-list">
              <li>Teeth Whitening</li><li>General Dentistry</li><li>Childrens Dentistry</li>
            </ul>
          </div>
          <div class="social" aria-hidden="true"><span></span><span></span></div>
          <p class="services-web">www.morveldental.com.au</p>
        </div>
      </div>
    </div>
  </section>

</main>
</body>
</html>
```